Webdesign für Sexualpädagogik
Zielgruppe
- Sexualpädagogik, Beratung und Sexualtherapie
- Vorträge und Seminare für Unternehmen / Institutionen Vorträge Sexualität in der Pflege / im Alter / Grenzen wahrnehmen
- Wechseljahreberatung, Beratung in der Lebensmitte
- ZIelgruppe: Menschen, die sich weiternetwickeln möchten, die Problme mit ihrer Sexualität haben, Paare, Jugendliche
letztes Interview in der Zeitung: https://www.4927.ch/talbotenblatt/archiv/gespraech-im-fokus/beratung-endet-nicht-an-der-tuer-zur-klinik-hin/
Aufgabenstellung
- bestehende Internetseite siehe unten: Schrift ist Especial Key von Klarer Bogen
- auf dem Briefpapier bisher noch der Fachbuchhandel und Onlinhandel, aber beides nicht mehr
- Bilder zum Thema bereist vorhanden
- für Werbeflyer habe ich die Therapie in dunkelblau gehalten udn in der sexualpädagogik in hellblau
der wunderkiste wird aus der website entfernet

```html
<!DOCTYPE html>
<html lang="de">
<head>
<meta charset="utf-8">
<title>Klarer Bogen – News</title>
<link href="https://fonts.googleapis.com/css2?family=Montserrat:wght@300;400;600;700&display=swap" rel="stylesheet">
<style>
  :root {
    --ink: #000000;
    --paper: #ffffff;
    --nav-text: #bdbdbd;
    --nav-active: #ffffff;
    --accent-red: #e30613;
    --footer-text: #555555;
    --footer-strong: #111111;
    --hero-teal: #4f6f6a;
    --hero-skin: #b58a72;
    --plus-grey: #6d6d6d;
  }
  * { box-sizing: border-box; margin: 0; padding: 0; }
  html, body {
    width: 1040px; height: 1200px; overflow: hidden;
    background: var(--paper);
    font-family: "Montserrat", sans-serif;
  }
  .page { position: relative; width: 1040px; height: 1200px; }

  .main-nav {
    position: absolute; top: 0; left: 0; width: 1040px; height: 42px;
    background: var(--ink);
    display: flex; justify-content: center; align-items: center; gap: 14px;
    font-size: 11.5px; letter-spacing: 0.04em; text-transform: uppercase;
    color: var(--nav-text); font-weight: 400;
  }
  .main-nav .sep { color: #777; }
  .main-nav .active { color: var(--nav-active); font-weight: 700; }
  .main-nav .caret { display: inline-block; width: 0; height: 0; border-left: 4px solid transparent; border-right: 4px solid transparent; border-top: 5px solid var(--nav-text); margin-left: 6px; vertical-align: middle; }
  .main-nav .search { margin-left: 12px; }

  .hero-photo {
    position: absolute; top: 42px; left: 0; width: 1040px; height: 700px;
    background:
      radial-gradient(ellipse 260px 330px at 390px 260px, var(--hero-skin) 0%, rgba(181,138,114,0.6) 55%, rgba(181,138,114,0) 100%),
      linear-gradient(90deg, #5f7f79 0%, var(--hero-teal) 40%, #3f5f5b 75%, #2f4a47 100%);
  }
  .hero-fade {
    position: absolute; top: 570px; left: 0; width: 1040px; height: 180px;
    background: linear-gradient(180deg, rgba(255,255,255,0) 0%, rgba(255,255,255,0.85) 70%, var(--paper) 100%);
  }

  .brand {
    position: absolute; top: 100px; left: 0; width: 1040px; text-align: center; color: var(--paper);
  }
  .brand-name { font-weight: 300; font-size: 32px; letter-spacing: 0.06em; line-height: 1; }
  .brand-tagline { margin-top: 8px; font-size: 12px; font-weight: 400; word-spacing: 12px; }

  .social { position: absolute; top: 264px; left: 486px; display: flex; gap: 7px; }
  .social span { display: block; width: 27px; height: 27px; border-radius: 50%; background: var(--ink); }

  .news-grid {
    position: absolute; top: 375px; left: 99px;
    display: grid; grid-template-columns: repeat(3, 261px); grid-auto-rows: 261px;
    column-gap: 32px; row-gap: 25px;
  }
  .news-card { position: relative; overflow: hidden; color: var(--paper); }
  .news-card .card-media { position: absolute; inset: 0; }
  .news-card .card-text { position: absolute; left: 20px; right: 14px; bottom: 24px; }
  .card-date { font-size: 14.5px; font-weight: 400; text-transform: uppercase; margin-bottom: 2px; }
  .card-title { font-size: 20px; font-weight: 700; text-transform: uppercase; line-height: 1.2; }

  .media-gallery { background: linear-gradient(160deg, #d9d9d9 0%, #6a6a6a 45%, #222 100%); }
  .media-red { background: var(--accent-red); }
  .media-meadow { background: linear-gradient(170deg, #fbe7b0 0%, #dca450 45%, #8a5a1e 100%); }
  .media-figure { background: linear-gradient(180deg, #9a8f8a 0%, #4a3f3e 55%, #2a2222 100%); }
  .media-parrot { background: linear-gradient(150deg, #9cc36a 0%, #2f7fc4 45%, #e0b92a 80%, #3a6a2a 100%); }
  .media-heart { background: linear-gradient(180deg, #f2f2f2 0%, #e4e4e4 100%); }

  .load-more {
    position: absolute; top: 946px; left: 493px; width: 54px; height: 54px;
  }

  .site-footer {
    position: absolute; top: 1096px; left: 0; width: 1040px; text-align: center;
    font-size: 10px; letter-spacing: 0.03em; text-transform: uppercase; color: var(--footer-text);
  }
  .site-footer strong { color: var(--footer-strong); font-weight: 600; margin-left: 8px; }
</style>
</head>
<body>
<div class="page">
  <nav class="main-nav">
    <span>Startseite</span><span class="sep">/</span>
    <span>Über mich</span><span class="sep">/</span>
    <span>Was wir tun<i class="caret"></i></span><span class="sep">/</span>
    <span>Blog</span><span class="sep">/</span>
    <span class="active">News</span><span class="sep">/</span>
    <span>Seminare<i class="caret"></i></span><span class="sep">/</span>
    <span>Kontakt</span>
    <svg class="search" width="14" height="14" viewBox="0 0 14 14" aria-hidden="true">
      <circle cx="5.5" cy="5.5" r="4.3" fill="none" stroke="#bdbdbd" stroke-width="2"/>
      <line x1="8.8" y1="8.8" x2="13" y2="13" stroke="#bdbdbd" stroke-width="2.2"/>
    </svg>
  </nav>

  <div class="hero-photo" role="img" aria-label="Foto: Gesicht mit geschlossenen Augen unter Wasser mit Schaumblasen"></div>
  <div class="hero-fade"></div>

  <div class="brand">
    <div class="brand-name">KLARER BOGEN</div>
    <div class="brand-tagline">Sexualpädagogik Beratung Therapie</div>
  </div>

  <div class="social" aria-label="Soziale Netzwerke"><span></span><span></span></div>

  <section class="news-grid">
    <article class="news-card">
      <div class="card-media media-gallery" role="img" aria-label="Schwarzweissfoto eines Innenraums mit Fenster und Pflanze"></div>
      <div class="card-text"><div class="card-date">Januar 2007</div><div class="card-title">Ausstellung über Sex-Zwangsarbeit im KZ</div></div>
    </article>
    <article class="news-card">
      <div class="card-media media-red"></div>
      <div class="card-text"><div class="card-date">Juni 2017</div><div class="card-title">» Ich mache aus jedem einen guten Liebhaber «</div></div>
    </article>
    <article class="news-card">
      <div class="card-media media-meadow" role="img" aria-label="Foto: Gräser im warmen Gegenlicht"></div>
      <div class="card-text"><div class="card-date">November 2006</div><div class="card-title">Tageslicht stei-<br>gert Lust auf Sex</div></div>
    </article>
    <article class="news-card">
      <div class="card-media media-figure" role="img" aria-label="Foto: Person im dunklen Mantel hält eine Ananas"></div>
      <div class="card-text"><div class="card-date">Januar 2007</div><div class="card-title">Let's talk about sex</div></div>
    </article>
    <article class="news-card">
      <div class="card-media media-parrot" role="img" aria-label="Foto: bunter Papagei"></div>
      <div class="card-text"><div class="card-date">August 2008</div><div class="card-title">Papagei verriet Besitzer Liebesaffäre seiner Freundin</div></div>
    </article>
    <article class="news-card">
      <div class="card-media media-heart" role="img" aria-label="Foto: rotes Papierherz an einer Schnur"></div>
      <div class="card-text"><div class="card-date">Juni 2006</div><div class="card-title">Klarer Bogen ge-<br>winnt 2. Platz<br>beim Innovations -<br>und Ideenwettbe-<br>werb für Jungun-<br>ternehmer</div></div>
    </article>
  </section>

  <svg class="load-more" viewBox="0 0 54 54" aria-label="Mehr laden">
    <circle cx="27" cy="27" r="25.5" fill="none" stroke="#6d6d6d" stroke-width="2"/>
    <line x1="27" y1="9" x2="27" y2="45" stroke="#6d6d6d" stroke-width="1.5"/>
    <line x1="9" y1="27" x2="45" y2="27" stroke="#6d6d6d" stroke-width="1.5"/>
  </svg>

  <footer class="site-footer">©2018 Klarer-Bogen <strong>Datenschutzerklärung</strong> <strong>Impressum</strong></footer>
</div>
</body>
</html>
```